Qivera Health & Wellness Business Card Design

We would like to create business cards matching with our new logo design. The card should be professional looking but still have a playful side and something that would be eye catching. We are planing to open a luxury medical spa and looking to create a design based on this new logo. We are looking for a design that shows off luxury but not be gold in color. Also, while we are a more female oriented medical center we do have men that come in for our services and it should be be too feminine.

Target Market(s)

Health & Wellness. Medical patients. Luxury spa

Industry/Entity Type

Health And Wellness

Contact Information for Business Card

It should have the logo design in the front of card and back of card should have our contact information. Our current colors are peach/ coral, teal, and gray. We are looking for a modern looking design.

Font styles to use
Script

Colors
32a6d6
e667a6
86cfc6
fece3e

Requirements
Must have
• It should have our logo design. We would prefer to have a more modern look to the card.
Nice to have
• Eye-Catching Design on the personable side but still classy.
Should not have
• At this point we are looking for the best design. It should not have color purple.

```html
<!DOCTYPE html>
<html lang="en">
<head>
<meta charset="utf-8">
<title>Qivera Health &amp; Wellness Business Card</title>
<link rel="stylesheet" href="https://fonts.googleapis.com/css2?family=Montserrat:wght@400;500;600&display=swap">
<style>
  :root {
    --canvas-bg: #e9e7e5;
    --ink: #0b0b0b;
    --paper: #ffffff;
    --muted: #2a2a2a;
    --rule: #1a1a1a;
  }
  * { margin: 0; padding: 0; box-sizing: border-box; }
  html, body { width: 1200px; height: 831px; overflow: hidden; }
  body {
    background: var(--canvas-bg);
    font-family: "Montserrat", Arial, sans-serif;
    position: relative;
  }
  .card {
    position: absolute;
    top: 265px;
    width: 520px;
    height: 300px;
    overflow: hidden;
    box-shadow: 0 6px 18px rgba(0,0,0,0.18);
  }
  .card-front { left: 50px; background: var(--ink); }
  .card-back  { left: 630px; background: var(--paper); }

  .brand {
    position: absolute;
    display: flex;
    flex-direction: column;
    gap: 6px;
    font-weight: 500;
  }
  .card-front .brand { left: 140px; top: 100px; color: var(--paper); }
  .card-back .brand  { left: 62px; top: 88px; color: var(--ink); }
  .brand-name { font-size: 44px; line-height: 1; letter-spacing: 1px; }
  .card-back .brand-name { font-size: 34px; }
  .brand-tagline { font-size: 14px; letter-spacing: 0.5px; }
  .card-back .brand-tagline { font-size: 11px; }

  .divider {
    position: absolute;
    left: 262px;
    top: 78px;
    width: 2px;
    height: 104px;
    background: var(--rule);
  }
  .contact {
    position: absolute;
    left: 282px;
    top: 84px;
    color: var(--ink);
  }
  .contact-name { font-size: 19px; font-weight: 600; line-height: 1.1; }
  .contact-title { font-size: 14px; font-weight: 400; color: var(--muted); margin-bottom: 8px; }
  .contact-list { list-style: none; }
  .contact-item {
    display: flex;
    align-items: center;
    gap: 8px;
    font-size: 14px;
    line-height: 20px;
  }
  .contact-item svg { width: 11px; height: 11px; fill: var(--ink); flex: none; }

  .wave { position: absolute; left: 0; top: 0; }
</style>
</head>
<body>

  <section class="card card-front" aria-label="Card front">
    <div class="brand">
      <span class="brand-name">Qivera</span>
      <span class="brand-tagline">Health, Wellness &amp; Beauty</span>
    </div>
  </section>

  <section class="card card-back" aria-label="Card back">
    <svg class="wave" width="520" height="300" viewBox="0 0 520 300" aria-hidden="true">
      <path d="M0,150 C18,232 150,252 300,266 C400,276 470,288 520,300 L0,300 Z" fill="#0b0b0b"/>
      <path d="M0,178 C40,238 190,262 370,286" fill="none" stroke="#ffffff" stroke-width="5" stroke-linecap="round"/>
    </svg>

    <div class="brand">
      <span class="brand-name">Qivera</span>
      <span class="brand-tagline">Health, Wellness &amp; Beauty</span>
    </div>

    <div class="divider"></div>

    <div class="contact">
      <p class="contact-name">Your Name</p>
      <p class="contact-title">Your Title</p>
      <ul class="contact-list">
        <li class="contact-item">
          <svg viewBox="0 0 24 24"><path d="M6.6 10.8a15.1 15.1 0 0 0 6.6 6.6l2.2-2.2c.3-.3.7-.4 1-.2 1.1.4 2.3.6 3.6.6.6 0 1 .4 1 1V20c0 .6-.4 1-1 1A17 17 0 0 1 3 4c0-.6.4-1 1-1h3.5c.6 0 1 .4 1 1 0 1.3.2 2.5.6 3.6.1.3 0 .7-.2 1z"/></svg>
          <span>123-456-2100</span>
        </li>
        <li class="contact-item">
          <svg viewBox="0 0 24 24"><path d="M2 5h20v14H2z M3 6l9 7 9-7" fill="#0b0b0b"/><path d="M3 6.5l9 6.5 9-6.5" stroke="#fff" stroke-width="1.6" fill="none"/></svg>
          <span>youremail@qiveramail.com</span>
        </li>
        <li class="contact-item">
          <svg viewBox="0 0 24 24"><circle cx="12" cy="12" r="10"/><path d="M2 12h20M12 2c3 3 3 17 0 20M12 2c-3 3-3 17 0 20" stroke="#fff" stroke-width="1.5" fill="none"/></svg>
          <span>www.yourwebsite.com</span>
        </li>
      </ul>
    </div>
  </section>

</body>
</html>
```